New Website Design for PALVO.org

We are looking for a new website design for PALVO.org. PALVO is a non profit home inspector association based in California. Home Inspectors are people that come out and look at a house before it's purchased to let the buyer know of any defects that may exist.
Our site is based on Joomla so if you'll be able to make a Joomla 3 template as well, please let us know (not required, but a bonus).
We would like to see designs that incorporate royal blue, white and chrome into the site as that's our main business colors.
We would like a place for rotating banners though they don't need to be the same size as the current site.
We would like navigation to be easier to manage with menus only across the top (via drop down menus) where we are going to sort out the items currently on the side. Possibly the front page could have a graphic link to separate portals for Realtors, Home Buyers and Inspectors, but that's just one option.
We would like a good mobile design or something that will scale easily to mobile.
The Find an Inspector feature is important and should stand out. The ZIM PALVOr site
Current home page feels a bit busy. Would like to simplify a bit.

```html
<!DOCTYPE html>
<html lang="en">
<head>
<meta charset="utf-8">
<title>PALVO – Home</title>
<link href="https://fonts.googleapis.com/css2?family=PT+Sans:wght@400;700&family=PT+Sans+Narrow:wght@400;700&display=swap" rel="stylesheet">
<style>
:root{
  --royal:#4367b0;
  --royal-dark:#34589c;
  --ink:#2a2a2a;
  --text:#555;
  --page:#efefef;
  --white:#fff;
  --rule:#d9d9d9;
  --footer-top:#2f3235;
  --footer-bottom:#1f2224;
  --footer-text:#e4e4e4;
  --footer-head:#4f74c0;
}
*{margin:0;padding:0;box-sizing:border-box}
html,body{width:1106px;height:1200px;overflow:hidden}
body{background:var(--page);font-family:"PT Sans",sans-serif;color:var(--text);position:relative}
.abs{position:absolute}

.site-header{position:absolute;left:0;top:0;width:1106px;height:83px;background:var(--white)}
.brand{position:absolute;left:160px;top:10px;display:flex;align-items:center}
.brand-mark{width:64px;height:64px;border-radius:50%;border:3px solid #8a9bbd;background:#f4f6fa}
.brand-text{margin-left:10px}
.brand-name{font-size:24px;color:var(--ink);line-height:1.1}
.brand-tagline{font-size:7.5px;color:var(--royal);text-transform:uppercase;letter-spacing:.6px;margin-top:3px;margin-left:2px}
.social-dots{position:absolute;left:858px;top:23px;display:flex;gap:8px}
.social-dots span{width:24px;height:24px;border-radius:50%;display:block}
.dot-a{background:#164a7e}.dot-b{background:#2aa6e1}.dot-c{background:#f29111}
.phone{position:absolute;left:856px;top:51px;font-size:13.5px;color:#6f84b6;letter-spacing:.3px}

.main-nav{position:absolute;left:0;top:83px;width:1106px;height:41px;background:var(--royal)}
.main-nav ul{list-style:none;position:absolute;left:158px;width:789px;top:0;height:41px;display:flex;justify-content:space-between;align-items:center}
.main-nav li{font-size:11.5px;color:var(--white);letter-spacing:.6px}
.main-nav li.current{color:#1b2540}
.main-nav li.sep{color:#dfe6f5}

.page{position:absolute;left:158px;top:124px;width:789px;height:826px;background:var(--white);box-shadow:0 0 3px rgba(0,0,0,.15)}

.hero{position:absolute;left:7px;top:6px;width:773px;height:274px;background:linear-gradient(180deg,#b9c9d8 0%,#d8dfe3 35%,#a9adab 60%,#5f7a43 100%)}
.hero-card{position:absolute;left:41px;top:36px;width:258px;height:205px;background:rgba(240,240,240,.9);padding:12px 11px}
.hero-card h1{font-weight:400;font-size:19px;line-height:26px;color:var(--ink)}
.hero-card p{font-family:"PT Sans Narrow",sans-serif;font-size:10.5px;line-height:17.5px;color:#444;margin-top:11px}
.btn{display:inline-block;background:var(--royal);color:var(--white);font-family:"PT Sans Narrow",sans-serif;font-size:12px;width:78px;height:31px;line-height:31px;text-align:center;margin-top:14px}

.welcome{position:absolute;left:0;top:287px;width:789px;height:199px;background:var(--royal)}
.welcome h2{position:absolute;left:26px;top:14px;font-weight:400;font-size:19px;color:var(--white)}
.welcome-photo{position:absolute;left:28px;top:51px;width:242px;height:126px;background:#ececec;padding:7px}
.welcome-photo div{width:100%;height:100%;background:linear-gradient(135deg,#8fb1d6 0%,#d9d9d4 45%,#5a6c4a 100%)}
.welcome-text{position:absolute;left:297px;top:50px;width:458px;font-family:"PT Sans Narrow",sans-serif;font-size:12px;line-height:22px;color:var(--white)}
.welcome-text .more{color:#e6ecf8;margin-left:6px}

.portals-head{position:absolute;left:21px;top:519px;font-size:16px;color:var(--royal);letter-spacing:.3px}
.portals-rule{position:absolute;left:160px;top:522px;width:612px;height:1px;background:var(--rule)}
.portal{position:absolute;top:544px;width:176px}
.portal-photo{width:176px;height:113px;border:1px solid #e2e2e2;background:#f7f7f7;padding:6px}
.portal-photo div{width:100%;height:100%}
.portal-title{margin-top:6px;display:flex;align-items:center;font-size:9px;color:var(--royal);letter-spacing:.5px;text-transform:uppercase;padding-bottom:5px;border-bottom:1px solid var(--rule)}
.portal-title i{width:9px;height:9px;border-radius:50%;border:2.5px solid var(--royal);margin:0 5px 0 2px;display:block}
.portal p{font-family:"PT Sans Narrow",sans-serif;font-size:10px;line-height:18px;color:var(--text);margin-top:5px}
.portal .more{font-family:"PT Sans Narrow",sans-serif;font-size:10px;color:var(--ink);margin-top:7px;display:flex;align-items:center;gap:4px}

.site-footer{position:absolute;left:158px;top:950px;width:789px;height:236px;background:linear-gradient(180deg,var(--footer-top),var(--footer-bottom));color:var(--footer-text)}
.footer-bar{position:absolute;left:158px;top:1178px;width:789px;height:8px;background:var(--royal)}
.f-head{position:absolute;top:41px;font-size:10px;color:var(--footer-head);text-transform:uppercase;letter-spacing:.3px}
.f-rule{position:absolute;top:57px;height:1px;background:#4a4d50}
.sitemap{position:absolute;top:68px;list-style:none;font-size:9.5px;line-height:19px}
.sitemap li::before{content:"›";color:var(--footer-head);font-weight:700;margin-right:10px}
.follow{position:absolute;left:292px;top:73px;display:grid;grid-template-columns:repeat(3,30px);column-gap:38px;row-gap:10px}
.follow span{width:30px;height:30px;border-radius:50%;background:radial-gradient(circle at 40% 35%,#f2f2f2,#9a9a9a);display:block}
.copyright{position:absolute;left:290px;top:158px;font-size:8.5px;letter-spacing:.4px;color:#ddd}
.copyright b{font-weight:400;color:var(--footer-head)}
.contact label{position:absolute;left:564px;font-size:9px;color:#ddd}
.contact .field{position:absolute;left:604px;width:165px;background:#26292b;border:1px solid #44484b}
.go{position:absolute;left:605px;top:162px;width:47px;height:21px;background:linear-gradient(180deg,#5579c4,#2f55a3);color:var(--white);font-size:9.5px;text-align:center;line-height:21px;letter-spacing:1px}
</style>
</head>
<body>

<header class="site-header">
  <div class="brand">
    <div class="brand-mark"></div>
    <div class="brand-text">
      <div class="brand-name">Pacific Association of Licensed Visual Observers</div>
      <div class="brand-tagline">We look at a house before it's purchased to let the buyer know of any issues.</div>
    </div>
  </div>
  <div class="social-dots"><span class="dot-a"></span><span class="dot-b"></span><span class="dot-c"></span></div>
  <div class="phone">(800) 555-0147</div>
</header>

<nav class="main-nav">
  <ul>
    <li class="current">HOME</li><li class="sep">|</li>
    <li>FIND AN INSPECTOR</li><li class="sep">|</li>
    <li>HOME BUYERS &amp; SELLERS</li><li class="sep">|</li>
    <li>REAL ESTATE AGENTS</li><li class="sep">|</li>
    <li>INSPECTORS</li><li class="sep">|</li>
    <li>ASK PALVO</li><li class="sep">|</li>
    <li>CONFERENCES</li>
  </ul>
</nav>

<main class="page">
  <section class="hero" role="img" aria-label="Photo of three inspectors standing in front of a white two-storey house">
    <div class="hero-card">
      <h1>Lorem Ipsum Dolor Sitame<br>Consectetur Allan</h1>
      <p>The Pacific Association of Licensed Visual Observers (PALVO) is a voluntary, nonprofit public-benefit organization of real estate inspectors. PALVO provides education, training and support services to its members.</p>
      <span class="btn">read more</span>
    </div>
  </section>

  <section class="welcome">
    <h2>Welcome to PALVO</h2>
    <div class="welcome-photo"><div role="img" aria-label="Photo of an inspector and a client reviewing documents outside a house"></div></div>
    <p class="welcome-text">The Pacific Association of Licensed Visual Observers (PALVO) is a voluntary, nonprofit public-benefit organization of real estate inspectors. Founded in 1976, PALVO provides education, training and support services to its members and the real estate community.<br>PALVO's Code of Ethics and Standards of Practice are recognized by the California Business and Professions Codes and are considered the standard of care by the real estate industry and legal profession in the state. <span class="more">read more ▸</span></p>
  </section>

  <h3 class="portals-head">Website portals</h3>
  <div class="portals-rule"></div>

  <article class="portal" style="left:15px">
    <div class="portal-photo"><div role="img" aria-label="Photo of smiling realtors" style="background:linear-gradient(135deg,#d9b49a,#8c98b0 55%,#e07a8a)"></div></div>
    <div class="portal-title"><i></i>Realtors</div>
    <p>Lorem ipsum dolor sit amet, consectetur adipising elit. Praesent dolor nunc, rhoncus porttitorol bibendum in, placerat sed dui raesent suscipiten consequat nunc.</p>
    <div class="more">read more <svg width="10" height="6" viewBox="0 0 10 6"><path d="M0 3h9M6 0.5 9 3 6 5.5" stroke="#2a2a2a" fill="none"/></svg></div>
  </article>
  <article class="portal" style="left:209px">
    <div class="portal-photo"><div role="img" aria-label="Photo of a couple with moving boxes" style="background:linear-gradient(135deg,#e4e4e4,#8a8fa8 55%,#c49a6c)"></div></div>
    <div class="portal-title"><i></i>Home Buyers</div>
    <p>Lorem ipsum dolor sit amet, consectetur adipising elit. Praesent dolor nunc, rhoncus porttitorol bibendum in, placerat sed dui raesent suscipiten consequat nunc.</p>
    <div class="more">read more <svg width="10" height="6" viewBox="0 0 10 6"><path d="M0 3h9M6 0.5 9 3 6 5.5" stroke="#2a2a2a" fill="none"/></svg></div>
  </article>
  <article class="portal" style="left:404px">
    <div class="portal-photo"><div role="img" aria-label="Photo of an inspector holding a folder in front of a house" style="background:linear-gradient(135deg,#9fb9d8,#c9c3b6 50%,#4a4f58)"></div></div>
    <div class="portal-title"><i></i>Inspectors</div>
    <p>Lorem ipsum dolor sit amet, consectetur adipising elit. Praesent dolor nunc, rhoncus porttitorol bibendum in, placerat sed dui raesent suscipiten consequat nunc.</p>
    <div class="more">read more <svg width="10" height="6" viewBox="0 0 10 6"><path d="M0 3h9M6 0.5 9 3 6 5.5" stroke="#2a2a2a" fill="none"/></svg></div>
  </article>
  <article class="portal" style="left:598px">
    <div class="portal-photo"><div role="img" aria-label="Photo of a stack of publications" style="background:linear-gradient(180deg,#f1f1f1,#d7d9de 50%,#b7bccb)"></div></div>
    <div class="portal-title"><i></i>Educational Publications</div>
    <p>Lorem ipsum dolor sit amet, consectetur adipising elit. Praesent dolor nunc, rhoncus porttitorol bibendum in, placerat sed dui raesent suscipiten consequat nunc.</p>
    <div class="more">read more <svg width="10" height="6" viewBox="0 0 10 6"><path d="M0 3h9M6 0.5 9 3 6 5.5" stroke="#2a2a2a" fill="none"/></svg></div>
  </article>
</main>

<footer class="site-footer">
  <div class="f-head" style="left:26px">Sitemap</div>
  <div class="f-rule" style="left:26px;width:212px"></div>
  <ul class="sitemap" style="left:34px">
    <li>Lorem Ipsum</li><li>Entring</li><li>Solop Ichte</li><li>Opole</li><li>Devrdrics</li><li>Obsoe Palax</li>
  </ul>
  <ul class="sitemap" style="left:156px">
    <li>Ferencg Quino</li><li>Susip</li><li>Pnchat Yipol</li><li>Sushiti Oppse</li><li>Fertin Singe</li><li>Poq Weloom</li>
  </ul>

  <div class="f-head" style="left:292px">Follow us</div>
  <div class="f-rule" style="left:292px;width:212px"></div>
  <div class="follow"><span></span><span></span><span></span><span></span><span></span><span></span></div>
  <div class="copyright">© Copyright <b>business</b> 2012 &nbsp;|&nbsp; All rights reserved</div>

  <div class="f-head" style="left:563px">Contact us</div>
  <div class="f-rule" style="left:563px;width:206px"></div>
  <div class="contact">
    <label style="top:68px">Name</label><div class="field" style="top:64px;height:20px"></div>
    <label style="top:92px">Email</label><div class="field" style="top:88px;height:20px"></div>
    <label style="top:116px">Message</label><div class="field" style="top:114px;height:42px"></div>
    <div class="go">GO</div>
  </div>
</footer>
<div class="footer-bar"></div>

</body>
</html>
```